Marlow Poise & Image Consultancy

Hi, I need a brochure design for my personal styling business. I have downloaded the company logo along with the content of the services offered for the brochure. Being a colour and styling business I would been keen on having some pictures of timeless fashion or colour samples, This is not absolutely necessary just an idea. I had also thought about changing and naming the services offered with a feminine, fun interesting type of theme. This may make it more inviting, I would be really interested in any of your creative ideas in this area. I will be deciding on the business card design in the next couple of days. I will download the design for this once I have made the decision. I will be okay to pay for any photo images that may be required if the brochure is selected. I had envisaged a tri fold brochure standard letter size with two folds (8.5" by 11inchs) however I am open to any suggestions. Please feel free to make any changes or modification's to the content, font etc in the files downloaded for the brochure. Many Thanks.
Updates
Project Deadline Extended
Reason: I need to extend the time for this project as I do not have all of content required for the brochure confirmed. Many Thanks
Industry/Entity Type
Fashion
Font styles to use
Look and feel
Each slider illustrates characteristics of the customer's brand and the style your logo design should communicate.

```html
<!DOCTYPE html>
<html lang="en">
<head>
<meta charset="utf-8">
<title>Marlow Poise &amp; Image Consultancy – Tri-fold Brochure</title>
<link rel="stylesheet" href="https://fonts.googleapis.com/css2?family=Ubuntu:wght@400;500&display=swap">
<style>
  :root {
    --amber: #f5a814;
    --paper: #ffffff;
    --ink: #2b2b2b;
    --ink-soft: #4a4a4a;
    --rule-grey: #6d6d6d;
    --backdrop: #ecebe8;
  }
  * { box-sizing: border-box; margin: 0; padding: 0; }
  html, body {
    width: 1200px; height: 960px; overflow: hidden;
    background: var(--backdrop);
    font-family: "Ubuntu", Arial, sans-serif;
    color: var(--ink);
  }
  .brochure {
    position: absolute; left: 50px; top: 55px;
    width: 1100px; height: 850px;
    display: flex;
    box-shadow: 0 6px 24px rgba(0,0,0,.18);
  }
  .panel { position: relative; width: 366.67px; height: 100%; overflow: hidden; }
  .panel--services { background: var(--paper); }
  .panel--office { background: var(--amber); }
  .panel--cover { background: var(--paper); }

  /* Services panel */
  .service-notes { list-style: none; padding: 34px 28px 0 30px; }
  .service-notes li {
    position: relative; padding-left: 16px; margin-bottom: 12px;
    font-size: 12.5px; line-height: 1.45; color: var(--ink-soft);
  }
  .service-notes li::before, .service-list li::before {
    content: ""; position: absolute; left: 0; top: 4px;
    border-left: 8px solid var(--amber);
    border-top: 4.5px solid transparent; border-bottom: 4.5px solid transparent;
  }
  .friends-photo {
    position: absolute; left: 0; top: 200px; width: 100%; height: 240px;
    background: linear-gradient(160deg, #a9c98a 0%, #d9e8c4 35%, #c9a98e 65%, #7d8e6a 100%);
  }
  .service-list { list-style: none; position: absolute; left: 30px; top: 475px; }
  .service-list li {
    position: relative; padding-left: 16px;
    font-size: 12.5px; line-height: 24px; color: var(--ink-soft);
  }

  /* Office panel */
  .office-heading {
    position: absolute; left: 50px; right: 50px; top: 505px;
    text-align: center; font-size: 22px; font-weight: 400; color: var(--ink);
    padding-bottom: 6px;
  }
  .office-rule {
    position: absolute; left: 40px; right: 40px; top: 540px;
    border-top: 1.5px dashed var(--ink);
  }

  /* Cover panel */
  .brand {
    position: absolute; top: 38px; left: 0; right: 0; text-align: center;
  }
  .brand-mark {
    width: 46px; height: 46px; border-radius: 50%;
    background: var(--rule-grey); margin: 0 auto 10px;
  }
  .brand-name { font-size: 40px; font-weight: 400; color: var(--amber); line-height: 1; }
  .brand-tagline { font-size: 13px; color: var(--ink); margin-top: 6px; letter-spacing: .3px; }
  .cover-rule { position: absolute; left: 0; top: 240px; width: 100%; height: 60px; }
  .model-photo {
    position: absolute; left: 22px; right: 0; top: 300px; bottom: 0;
    background: linear-gradient(170deg, #f2f2f2 0%, #cfcfcf 30%, #4a4a4a 60%, #1c1c1c 100%);
  }
  .offer-tags { list-style: none; position: absolute; left: 0; right: 0; top: 470px; }
  .offer-tag {
    position: absolute; right: -4px; height: 36px;
    background: var(--amber); color: var(--ink);
    font-size: 18px; line-height: 36px; padding-left: 26px;
    clip-path: polygon(14px 0, 100% 0, 100% 100%, 14px 100%, 0 50%);
  }
  .offer-tag--consult { top: 0; left: 150px; }
  .offer-tag--shopping { top: 46px; left: 78px; }
  .offer-tag--hair { top: 92px; left: 8px; font-size: 17px; }
  .offer-tag--makeup { top: 138px; left: 92px; }
</style>
</head>
<body>
  <main class="brochure">
    <section class="panel panel--services">
      <ul class="service-notes">
        <li>Wardrobe Make over – Clear out and reassess your wardrobe to ensure it reflects your life style &amp; personality.</li>
        <li>Style Me Complete: Accessories &amp; Putting it all together – add the finishing touches to your look with the choice of shoes and accessories, your hair style &amp; make up</li>
      </ul>
      <div class="friends-photo" role="img" aria-label="Photo of three friends in sunglasses laughing outdoors among green trees"></div>
      <ul class="service-list">
        <li>Personal Shopping</li>
        <li>Make up Lessons</li>
        <li>Personal Shopping</li>
        <li>Special Occasion Make up</li>
        <li>Party &amp; Group Experiences</li>
        <li>Complete Makeovers</li>
        <li>Personal Styling Packages</li>
      </ul>
    </section>

    <section class="panel panel--office">
      <h2 class="office-heading">Our Office</h2>
      <div class="office-rule"></div>
    </section>

    <section class="panel panel--cover">
      <header class="brand">
        <div class="brand-mark"></div>
        <div class="brand-name">Marlow</div>
        <div class="brand-tagline">Poise &amp; Image Consultancy</div>
      </header>
      <svg class="cover-rule" viewBox="0 0 367 60" preserveAspectRatio="none" aria-hidden="true">
        <polygon points="0,4 367,22 367,30 0,8" fill="var(--amber)"/>
        <line x1="230" y1="38" x2="367" y2="30" stroke="var(--rule-grey)" stroke-width="2"/>
      </svg>
      <div class="model-photo" role="img" aria-label="Black and white fashion photo of a woman in sunglasses and a dark dress"></div>
      <ul class="offer-tags">
        <li class="offer-tag offer-tag--consult">Consultation</li>
        <li class="offer-tag offer-tag--shopping">Personal shopping service</li>
        <li class="offer-tag offer-tag--hair">Hair (accompaniment to hair salon)</li>
        <li class="offer-tag offer-tag--makeup">Make up Make over</li>
      </ul>
    </section>
  </main>
</body>
</html>
```